Entertainment Sound and Lighting company Business card

We need a professional looking business card designed for my growing entertainment sound and lighting company based in Sydney, Australia called "Kestrel Sound"

We provide technical production services (sound systems/lighting/vision) for events ranging from band gigs, weddings, corporate functions etc.

The business card needs to contain the following information:

Bartholomew Quenneville
Audio Engineer
Phone: 0478 615 702
Email: bartholomew@kestrelsound.com.au
Website: www.kestrelsound.com.au

Business logo has been attached in .ai format, please contact me if you need me to provide other files.

Target Market(s)

We need a business card that reflects our modern and professional company but still looks professional to appeal to our corporate clients.
We have a very broad target market spanning from bands needing PA systems for their gigs (18-30yrs) to event companies needing sound and lighting for weddings and other functions.

Industry/Entity Type

Business

Requirements
Must have
• Needs to include the logo that is attached of course, and the colour scheme.
Nice to have
• - Double sided

```html
<!DOCTYPE html>
<html lang="en">
<head>
<meta charset="utf-8">
<title>Kestrel Sound — Business Card</title>
<link rel="stylesheet" href="https://fonts.googleapis.com/css2?family=Crimson+Text:ital,wght@0,600;1,400&display=swap">
<style>
  :root {
    --sky: #00b8e2;
    --brand-blue: #0a8fcf;
    --paper: #ffffff;
    --backdrop: #ffffff;
    --shadow: rgba(0, 0, 0, 0.28);
  }
  * { margin: 0; padding: 0; box-sizing: border-box; }
  html, body {
    width: 964px;
    height: 1200px;
    overflow: hidden;
    background: var(--backdrop);
  }
  .sheet {
    position: relative;
    width: 964px;
    height: 1200px;
  }
  .card {
    position: absolute;
    left: 26px;
    width: 907px;
    height: 517px;
    box-shadow: 2px 4px 8px var(--shadow);
    font-family: "Crimson Text", "Times New Roman", serif;
    overflow: hidden;
  }
  .card--front { top: 23px; background: var(--paper); }
  .card--back { top: 645px; background: var(--sky); }
  .card__tabs {
    position: absolute;
    inset: 0;
    width: 100%;
    height: 100%;
  }
  .card__row {
    position: absolute;
    left: 0;
    width: 100%;
    text-align: center;
    transform: translateY(-50%);
    white-space: nowrap;
  }
  .brand-name {
    font-weight: 600;
    font-style: normal;
    font-size: 66px;
    letter-spacing: 0.5px;
    line-height: 1;
  }
  .card--front .brand-name { color: var(--brand-blue); top: 252px; }
  .card--back .brand-name { color: var(--paper); top: 176px; font-size: 52px; }
  .divider {
    position: absolute;
    left: 50%;
    height: 2px;
    transform: translateX(-50%);
  }
  .card--front .divider {
    top: 331px;
    width: 550px;
    background: linear-gradient(90deg, rgba(0,184,226,0) 0%, var(--sky) 50%, rgba(0,184,226,0) 100%);
  }
  .card--back .divider {
    top: 244px;
    width: 550px;
    background: linear-gradient(90deg, rgba(255,255,255,0) 0%, rgba(255,255,255,0.9) 50%, rgba(255,255,255,0) 100%);
  }
  .holder-name {
    font-style: italic;
    font-weight: 400;
    font-size: 27px;
    color: var(--sky);
    top: 374px;
  }
  .contact {
    font-style: italic;
    font-weight: 400;
    font-size: 29px;
    color: var(--paper);
    line-height: 1;
  }
  .contact--name { top: 288px; }
  .contact--role { top: 329px; }
  .contact--phone { top: 370px; }
  .contact--email { top: 411px; }
  .contact--web { top: 452px; }
</style>
</head>
<body>
<main class="sheet">
  <section class="card card--front" aria-label="Business card front">
    <svg class="card__tabs" viewBox="0 0 875 499" preserveAspectRatio="none" aria-hidden="true">
      <path d="M223 0 H670 L652 22 Q447 8 240 22 Z" fill="var(--sky)"/>
      <path d="M223 499 H670 L655 478 Q447 468 238 478 Z" fill="var(--sky)"/>
    </svg>
    <div class="card__row brand-name">Kestrel Sound</div>
    <div class="divider"></div>
    <div class="card__row holder-name">Bartholomew Quenneville</div>
  </section>

  <section class="card card--back" aria-label="Business card back">
    <svg class="card__tabs" viewBox="0 0 875 499" preserveAspectRatio="none" aria-hidden="true">
      <path d="M218 0 H670 L652 22 Q447 4 236 22 Z" fill="var(--paper)"/>
      <path d="M218 499 H670 L652 477 Q447 468 236 477 Z" fill="var(--paper)"/>
    </svg>
    <div class="card__row brand-name">Kestrel Sound</div>
    <div class="divider"></div>
    <div class="card__row contact contact--name">Bartholomew Quenneville</div>
    <div class="card__row contact contact--role">Audio Engineer</div>
    <div class="card__row contact contact--phone">Phone: 0478 615 702</div>
    <div class="card__row contact contact--email">Email: bartholomew@kestrelsound.com.au</div>
    <div class="card__row contact contact--web">Website: www.kestrelsound.com.au</div>
  </section>
</main>
</body>
</html>
```